Eye-catching & Glamorous Labels for Skincare Bottles & Jars

We need new labels designed for our product range as we have been dormant for a few years and are now rebranding Velora Grace - Kindly Made Skincare. The label sizes are defined in the attached word document. All products have either a bright silver or a matte silver lid pump/spray so please keep this in mind.

We are open to colours and invite you to create bright trendy labels which are coordinated with the logo attached. The logo is not of any specific colour so dark on light, light on dark, tone on tone - we like purple / duck egg blue / turquoise WITH matte silver, however stronger colours like navy plus maroon with matte silver is also a strong favourite. If you feel inspired by a colour you think would be appropriate to Velora Grace please feel free to have a go.

A front section for product information is required and the back should include relevant details ie ingredients, company info, and a note that there has been no testing on animals.

The serum bottle will require a front and back label on a clear label in a pale colour to coordinate with the rest of the range. Size for this label is 35mm top edge, 25mm bottom edge, height 45mm - I have attached a picture of the serum bottle as they were originally pad printed. Please don't hesitate to contact me for any further information. Good luck!

Target Market(s)

Educated professional women 30-45 who are regular skincare users and looking for beautiful skincare products without animal derived ingredients and animal testing

Industry/Entity Type

Skin Care Product

Font styles to use
Serif
Sans Serif
Decorative
Script

Colors

Designer to choose colors to be used in the design.

Requirements
Must have
• Velora Grace Logo - eye catching design - not too busy or cramped.
Nice to have
• Is it possible to create a background pattern using a very small image of the logo? Just a thought.

```html
<!DOCTYPE html>
<html lang="en">
<head>
<meta charset="utf-8">
<title>Velora Grace – Skincare Label Range</title>
<link rel="stylesheet" href="https://fonts.googleapis.com/css2?family=Open+Sans:wght@400&display=swap">
<style>
  :root {
    --page: #ffffff;
    --outline: #3a3a3a;
    --lavender: #8a73b4;
    --mint: #74c7a9;
    --teal: #00a88a;
    --leaf-grey: #d9d9d9;
    --label-light-text: #e8e8e8;
    --label-dark-text: #111111;
  }
  html, body {
    margin: 0;
    padding: 0;
    width: 1200px;
    height: 1200px;
    overflow: hidden;
    background: var(--page);
  }
  .range {
    display: block;
    width: 1200px;
    height: 1200px;
  }
  .container-outline {
    fill: none;
    stroke: var(--outline);
    stroke-width: 1.2;
  }
  .container-body { fill: #ffffff; stroke: var(--outline); stroke-width: 1.2; }
  .label-lavender { fill: var(--lavender); }
  .label-mint { fill: var(--mint); }
  .label-teal { fill: var(--teal); }
  .brand-name,
  .product-name {
    font-family: "Open Sans", sans-serif;
    font-weight: 400;
    text-anchor: middle;
  }
  .on-light { fill: var(--label-light-text); }
  .on-dark { fill: var(--label-dark-text); }
  .brand-name { font-size: 21px; }
  .product-name { font-size: 19px; letter-spacing: 0.3px; }
  .jar .brand-name { font-size: 17px; }
  .jar .product-name { font-size: 16px; }
</style>
</head>
<body>
<svg class="range" viewBox="0 0 1040 1040" xmlns="http://www.w3.org/2000/svg" role="group" aria-label="Velora Grace skincare label range">
  <defs>
    <linearGradient id="leaf-on-lavender-tr" x1="0" y1="1" x2="1" y2="0">
      <stop offset="0" stop-color="#8a73b4"/>
      <stop offset="1" stop-color="#d9d9d9"/>
    </linearGradient>
    <linearGradient id="leaf-on-lavender-bl" x1="1" y1="0" x2="0" y2="1">
      <stop offset="0" stop-color="#8a73b4"/>
      <stop offset="1" stop-color="#cfcfd6"/>
    </linearGradient>
    <linearGradient id="leaf-on-mint-tr" x1="0" y1="1" x2="1" y2="0">
      <stop offset="0" stop-color="#74c7a9"/>
      <stop offset="1" stop-color="#d9d9d9"/>
    </linearGradient>
    <linearGradient id="leaf-on-mint-bl" x1="1" y1="0" x2="0" y2="1">
      <stop offset="0" stop-color="#74c7a9"/>
      <stop offset="1" stop-color="#d4d9d7"/>
    </linearGradient>
    <linearGradient id="leaf-on-teal-l" x1="1" y1="0" x2="0" y2="1">
      <stop offset="0" stop-color="#00a88a"/>
      <stop offset="1" stop-color="#cfd8d5"/>
    </linearGradient>
    <linearGradient id="leaf-on-teal-r" x1="0" y1="1" x2="1" y2="0">
      <stop offset="0" stop-color="#00a88a"/>
      <stop offset="1" stop-color="#d6dbd9"/>
    </linearGradient>
  </defs>

  <!-- Day & Night Cream bottle -->
  <g class="bottle bottle-cream">
    <rect class="container-outline" x="93" y="168" width="127" height="52"/>
    <rect class="container-outline" x="92" y="220" width="128" height="72"/>
    <polyline class="container-outline" points="96,232 215,228 120,246 218,244 110,262 214,258 136,276 218,272"/>
    <path class="container-body" d="M92,292 L92,305 L62,305 Q55,305 55,315 L55,775 Q55,785 65,785 L252,785 Q262,785 262,775 L262,315 Q262,305 252,305 L220,305 L220,292 Z"/>
    <rect class="label-lavender" x="55" y="312" width="207" height="430"/>
    <rect x="120" y="312" width="142" height="170" fill="url(#leaf-on-lavender-tr)" role="img" aria-label="Cluster of pale grey leaves in the top right corner"/>
    <rect x="55" y="672" width="100" height="70" fill="url(#leaf-on-lavender-bl)" role="img" aria-label="Small pale grey leaves in the lower left corner"/>
    <text class="brand-name on-light" x="158" y="512">Velora Grace</text>
    <text class="product-name on-light" x="158" y="582">DAY</text>
    <text class="product-name on-light" x="158" y="612">&amp;</text>
    <text class="product-name on-light" x="158" y="642">NIGHT</text>
    <text class="product-name on-light" x="158" y="672">CREAM</text>
  </g>

  <!-- Toner & Cleanser bottle -->
  <g class="bottle bottle-toner">
    <rect class="container-outline" x="367" y="152" width="118" height="55"/>
    <rect class="container-outline" x="370" y="207" width="112" height="70"/>
    <polyline class="container-outline" points="372,216 478,212 380,228 482,226 372,238 480,236 390,248 478,246"/>
    <path class="container-body" d="M370,277 L370,290 L326,290 Q318,290 318,300 L318,777 Q318,787 328,787 L523,787 Q533,787 533,777 L533,300 Q533,290 523,290 L482,290 L482,277 Z"/>
    <rect class="label-mint" x="318" y="305" width="213" height="450"/>
    <rect x="348" y="305" width="183" height="170" fill="url(#leaf-on-mint-tr)" role="img" aria-label="Cluster of pale grey leaves along the top edge"/>
    <rect x="318" y="685" width="95" height="70" fill="url(#leaf-on-mint-bl)" role="img" aria-label="Small pale grey leaves in the lower left corner"/>
    <text class="brand-name on-dark" x="425" y="518">Velora Grace</text>
    <text class="product-name on-dark" x="425" y="576">TONER</text>
    <text class="product-name on-dark" x="425" y="604">&amp;</text>
    <text class="product-name on-dark" x="425" y="634">CLEANSER</text>
  </g>

  <!-- Facial Scrub jar -->
  <g class="jar jar-scrub">
    <rect class="container-outline" x="595" y="533" width="383" height="65"/>
    <rect class="container-outline" x="598" y="598" width="377" height="42"/>
    <polyline class="container-outline" points="602,608 815,612 760,630 972,626"/>
    <path class="container-body" d="M598,640 L598,670 L590,670 Q580,670 580,680 L580,775 Q580,783 590,783 L980,783 Q990,783 990,775 L990,680 Q990,670 980,670 L975,670 L975,640 Z"/>
    <rect class="label-teal" x="582" y="675" width="406" height="95"/>
    <rect x="582" y="705" width="70" height="65" fill="url(#leaf-on-teal-l)" role="img" aria-label="Pale grey leaves at the left end of the band"/>
    <rect x="905" y="685" width="83" height="55" fill="url(#leaf-on-teal-r)" role="img" aria-label="Pale grey leaves at the right end of the band"/>
    <text class="brand-name on-light" x="780" y="728">Velora Grace</text>
    <text class="product-name on-light" x="780" y="762">FACIAL SCRUB</text>
  </g>
</svg>
</body>
</html>
```